Creative designs Needed! Dieting Tips for Nurses

Need a creative design for my first book that is targeted to nurses that want to lose weight.
THE TITLE OF MY BOOK IS:
The Bright Lantern Pantry Uprising:
9 Slim-Down Tricks Each Caregiver Should Learn!

- My audience is female.

- My colors for my business are red, black, gray and white however feel free to use other colors

- The cover should note there is Free Bonus Content.

- The book cover should have a fun modern feel to it.

- Since the title is talking about time. I think there should be some sort of clock in the design. Not an actual clock but a clock design.

- Please let me know if you need anything from me to complete your design. I go by Coach Brin.

- Subject of book is dieting tips for nurses

Target Market(s)

Nurses

Industry/Entity Type

Health And Wellness

Font styles to use
Serif

Colors
ec1f27
1b1b1b
dddddd

Requirements
Must have
• List the Free Bonus Content label on the front cover
• Must keep in mind there will be sequels to this book for other target markets
• • Should be creative, modern
• • Please try not to use stock images with just the text for this design - I am looking for something creative and unique.
• • Something that plays with the idea of time, think clock.
• • Need something out the box!!
• • Think diversity in the people if you do opt to use images - Would prefer if you steer clear of regular photos of people
• • If you do use an image of a nurse, please note nurses mostly wear scrubs today - so think about that in your concepts
Nice to have
• The design should be clever
Should not have
• Although I selected the 3 colors feel free to explore other colors and those 3 colors do not have to be the dominate colors.
• The book design should pop out to people when they see it.

```html
<!DOCTYPE html>
<html lang="en">
<head>
<meta charset="utf-8">
<title>The Bright Lantern Pantry Uprising</title>
<link href="https://fonts.googleapis.com/css2?family=Kaushan+Script&display=swap" rel="stylesheet">
<style>
  :root {
    --wood-dark: #2e1c12;
    --wood-mid: #5a3a26;
    --wood-warm: #6e4a30;
    --ink-white: #ffffff;
    --hand-steel: #d9dcdc;
    --brand-red: #ec1f27;
    --script: "Kaushan Script", cursive;
  }
  html, body {
    margin: 0;
    padding: 0;
    width: 752px;
    height: 1200px;
    overflow: hidden;
    background: var(--wood-dark);
  }
  .cover {
    position: relative;
    width: 752px;
    height: 1200px;
    overflow: hidden;
  }
  .food-table {
    position: absolute;
    inset: 0;
    background:
      radial-gradient(ellipse at 8% 70%, rgba(190, 60, 40, 0.55), transparent 30%),
      radial-gradient(ellipse at 95% 72%, rgba(200, 50, 40, 0.5), transparent 28%),
      radial-gradient(ellipse at 10% 15%, rgba(80, 120, 50, 0.5), transparent 30%),
      radial-gradient(ellipse at 90% 15%, rgba(210, 120, 50, 0.45), transparent 30%),
      radial-gradient(ellipse at 85% 95%, rgba(70, 120, 50, 0.5), transparent 30%),
      radial-gradient(ellipse at 12% 95%, rgba(170, 70, 70, 0.5), transparent 30%),
      linear-gradient(90deg, var(--wood-mid), var(--wood-warm) 50%, var(--wood-mid));
  }
  .clock-face {
    position: absolute;
    inset: 0;
  }
  .title {
    position: absolute;
    left: 0;
    top: 10px;
    width: 752px;
    margin: 0;
    font-family: var(--script);
    font-weight: 400;
    color: var(--ink-white);
    text-align: center;
    line-height: 1.1;
    font-size: 100px;
    transform: rotate(-7deg);
    transform-origin: center;
  }
  .title span { display: block; }
  .bonus-label {
    position: absolute;
    left: 470px;
    top: 752px;
    width: 150px;
    padding: 6px 0 8px;
    border: 3px solid var(--ink-white);
    border-radius: 14px;
    background: var(--brand-red);
    font-family: var(--script);
    font-size: 22px;
    line-height: 1.05;
    color: var(--ink-white);
    text-align: center;
    transform: rotate(-6deg);
  }
  .subtitle {
    position: absolute;
    left: 200px;
    top: 840px;
    width: 540px;
    margin: 0;
    font-family: var(--script);
    font-weight: 400;
    color: var(--ink-white);
    text-align: center;
    font-size: 54px;
    line-height: 1.15;
    transform: rotate(-6deg);
  }
  .subtitle span { display: block; }
</style>
</head>
<body>
  <main class="cover">
    <div class="food-table" role="img" aria-label="Overhead photo of fresh vegetables, fruit, seafood and meat around a dark wooden table"></div>

    <svg class="clock-face" width="752" height="1200" viewBox="0 0 752 1200" aria-hidden="true">
      <g fill="#ffffff">
        <circle cx="138" cy="664" r="10"/>
        <circle cx="676" cy="664" r="10"/>
        <circle cx="407" cy="400" r="6"/>
        <circle cx="541" cy="436" r="6"/>
        <circle cx="640" cy="534" r="6"/>
        <circle cx="640" cy="794" r="6"/>
        <circle cx="174" cy="534" r="6"/>
        <circle cx="174" cy="794" r="6"/>
        <circle cx="273" cy="436" r="6"/>
      </g>
      <g fill="var(--hand-steel)">
        <rect x="366" y="326" width="20" height="278" rx="10"/>
        <rect x="455" y="380" width="16" height="224" rx="8" transform="rotate(14 463 604)"/>
        <circle cx="376" cy="640" r="12"/>
      </g>
      <g stroke="#ffffff" stroke-width="3" stroke-linecap="round">
        <line x1="120" y1="860" x2="215" y2="880"/>
        <line x1="140" y1="1000" x2="230" y2="970"/>
        <line x1="250" y1="1130" x2="310" y2="1080"/>
        <line x1="600" y1="1110" x2="660" y2="1150"/>
        <line x1="690" y1="980" x2="740" y2="975"/>
        <line x1="640" y1="820" x2="700" y2="790"/>
      </g>
    </svg>

    <h1 class="title">
      <span>The Bright</span>
      <span>Lantern Pantry</span>
      <span>Uprising:</span>
    </h1>

    <div class="bonus-label">Free Bonus<br>Content</div>

    <p class="subtitle">
      <span>9 Slim-Down</span>
      <span>Tricks • Each</span>
      <span>Caregiver Should</span>
      <span>Learn!</span>
    </p>
  </main>
</body>
</html>
```